Houston Law Firm Business Card
Taven & Associates, PC 2013 Business Card
Professional
Dorian M. Taven
Trial Attorney
482 W. Birchfield Ave.
Suite 318
Houston, TX 77391
1-888-50-TAVEN
dorian.taven@tavenassociateslaw.example
tavenassociateslaw.example
Also include my blog:
lakeridgetrialcounsel.example

```html
<!DOCTYPE html>
<html lang="en">
<head>
<meta charset="utf-8">
<title>Taven &amp; Associates, PC — Business Cards</title>
<link rel="stylesheet" href="https://fonts.googleapis.com/css2?family=Arimo:wght@400;700&display=swap">
<style>
  :root{
    --stage:#2b2a28;
    --olive-light:#5c5b35;
    --olive-dark:#3b3a20;
    --ink:#1b1b1b;
    --ink-soft:#555;
    --paper:#ffffff;
    --paper-shade:#eeeeee;
    --black-light:#2a2a2a;
    --black-dark:#050505;
    --rule:#9a9a8a;
    --on-dark:#f2f2ea;
    --on-dark-soft:#d6d6c4;
  }
  *{box-sizing:border-box;margin:0;padding:0}
  html,body{width:1200px;height:758px;overflow:hidden;background:var(--stage)}
  body{font-family:"Arimo",Arial,sans-serif;position:relative}
  .card{position:absolute;width:494px;height:216px;overflow:hidden;box-shadow:0 4px 10px rgba(0,0,0,.5)}
  .card--back-olive{left:89px;top:89px}
  .card--back-white{left:610px;top:89px}
  .card--front-olive{left:89px;top:336px}
  .card--front-white{left:610px;top:336px}

  .card__head{position:absolute;left:0;top:0;width:100%;height:96px}
  .card__body{position:absolute;left:0;top:96px;width:100%;height:120px}
  .card--back-olive .card__head{background:linear-gradient(180deg,var(--paper),var(--paper-shade))}
  .card--back-olive .card__body{background:linear-gradient(180deg,var(--olive-light),var(--olive-dark));color:var(--on-dark)}
  .card--back-white .card__head{background:linear-gradient(180deg,var(--black-light),var(--black-dark))}
  .card--back-white .card__body{background:var(--paper);color:var(--ink)}

  .brand{position:absolute;display:flex;align-items:center;gap:12px}
  .brand__mark{width:22px;height:22px;background:currentColor;opacity:.55}
  .brand__name{font-size:17px;font-weight:400;letter-spacing:.5px;text-transform:uppercase;white-space:nowrap}
  .card__head .brand{left:24px;top:36px}
  .card--back-olive .brand{color:#555}
  .card--back-white .brand{color:#e8e8e8}

  .person{position:absolute;right:22px;top:6px;text-align:right}
  .person__name{font-size:13px;font-weight:700}
  .person__title{font-size:7.5px;margin-top:2px;opacity:.85}
  .person__rule{position:absolute;left:126px;right:132px;top:14px;height:1px;background:var(--rule)}

  .offices{position:absolute;left:14px;top:22px;font-size:7.5px;line-height:10px}
  .offices__label{font-weight:700;display:block;margin-top:6px}
  .offices__label:first-child{margin-top:0}

  .contact{position:absolute;right:14px;top:40px;font-size:7.5px;line-height:10.5px;text-align:right}
  .contact__row{display:flex;justify-content:flex-end;align-items:center;gap:5px}
  .contact__icon{width:7px;height:7px;flex:none}

  .card--front-olive{background:linear-gradient(180deg,var(--olive-light),var(--olive-dark));color:var(--on-dark)}
  .card--front-white{background:linear-gradient(180deg,var(--paper),var(--paper-shade));color:var(--ink)}
  .card--front-olive .brand,.card--front-white .brand{left:38px;top:52px}
  .card--front-olive .brand{color:var(--on-dark-soft)}
  .card--front-white .brand{color:#555}
  .front__rule{position:absolute;left:34px;right:34px;top:124px;height:1px}
  .card--front-olive .front__rule{background:rgba(255,255,255,.35)}
  .card--front-white .front__rule{background:#c8c8c8}
  .front__cities{position:absolute;left:38px;top:140px;font-size:15px;letter-spacing:.3px}
  .front__site{position:absolute;left:38px;top:178px;font-size:11px;letter-spacing:.3px;opacity:.75}
</style>
</head>
<body>

<section class="card card--back-olive">
  <div class="card__head">
    <div class="brand"><span class="brand__mark"></span><span class="brand__name">Taven &amp; Associates, PC</span></div>
  </div>
  <div class="card__body">
    <span class="person__rule"></span>
    <div class="person"><div class="person__name">Dorian M. Taven</div><div class="person__title">Trial Attorney</div></div>
    <div class="offices">
      <span class="offices__label">Houston Office:</span>482 W. Birchfield Ave., Suite 318<br>Houston, TX 77391
      <span class="offices__label">Sugar Land Office:</span>56 Maple Crest Center Blvd., Suite 210<br>Sugar Land, TX 77482
    </div>
    <div class="contact">
      <div class="contact__row">1-888-50-TAVEN<svg class="contact__icon" viewBox="0 0 10 10"><circle cx="5" cy="5" r="4" fill="currentColor"/></svg></div>
      <div class="contact__row">713.555.0142<svg class="contact__icon" viewBox="0 0 10 10"><circle cx="5" cy="5" r="4" fill="currentColor"/></svg></div>
      <div class="contact__row">713.555.0187<svg class="contact__icon" viewBox="0 0 10 10"><circle cx="5" cy="5" r="4" fill="currentColor"/></svg></div>
      <div class="contact__row">dorian.taven@tavenassociateslaw.example<svg class="contact__icon" viewBox="0 0 10 10"><rect x="1" y="2" width="8" height="6" fill="currentColor"/></svg></div>
      <div class="contact__row">lakeridgetrialcounsel.example<svg class="contact__icon" viewBox="0 0 10 10"><circle cx="5" cy="5" r="4" fill="none" stroke="currentColor" stroke-width="1.4"/></svg></div>
    </div>
  </div>
</section>

<section class="card card--back-white">
  <div class="card__head">
    <div class="brand"><span class="brand__mark"></span><span class="brand__name">Taven &amp; Associates, PC</span></div>
  </div>
  <div class="card__body">
    <span class="person__rule"></span>
    <div class="person"><div class="person__name">Dorian M. Taven</div><div class="person__title">Trial Attorney</div></div>
    <div class="offices">
      <span class="offices__label">Houston Office:</span>482 W. Birchfield Ave., Suite 318<br>Houston, TX 77391
      <span class="offices__label">Sugar Land Office:</span>56 Maple Crest Center Blvd., Suite 210<br>Sugar Land, TX 77482
    </div>
    <div class="contact">
      <div class="contact__row">1-888-50-TAVEN<svg class="contact__icon" viewBox="0 0 10 10"><circle cx="5" cy="5" r="4" fill="currentColor"/></svg></div>
      <div class="contact__row">713.555.0142<svg class="contact__icon" viewBox="0 0 10 10"><circle cx="5" cy="5" r="4" fill="currentColor"/></svg></div>
      <div class="contact__row">713.555.0187<svg class="contact__icon" viewBox="0 0 10 10"><circle cx="5" cy="5" r="4" fill="currentColor"/></svg></div>
      <div class="contact__row">dorian.taven@tavenassociateslaw.example<svg class="contact__icon" viewBox="0 0 10 10"><rect x="1" y="2" width="8" height="6" fill="currentColor"/></svg></div>
      <div class="contact__row">lakeridgetrialcounsel.example<svg class="contact__icon" viewBox="0 0 10 10"><circle cx="5" cy="5" r="4" fill="none" stroke="currentColor" stroke-width="1.4"/></svg></div>
    </div>
  </div>
</section>

<section class="card card--front-olive">
  <div class="brand"><span class="brand__mark"></span><span class="brand__name">Taven &amp; Associates, PC</span></div>
  <span class="front__rule"></span>
  <p class="front__cities">Houston • Sugar Land • New York</p>
  <p class="front__site">tavenassociateslaw.example</p>
</section>

<section class="card card--front-white">
  <div class="brand"><span class="brand__mark"></span><span class="brand__name">Taven &amp; Associates, PC</span></div>
  <span class="front__rule"></span>
  <p class="front__cities">Houston • Sugar Land • New York</p>
  <p class="front__site">tavenassociateslaw.example</p>
</section>

</body>
</html>
```